依頼詳細
<取扱商品>
レディースバレエシューズ・ルームシューズ・除菌スプレー・マスクケースなど

<ターゲット>
やや女性向け
基本は老若男女問わず

<使用画像について>
商品画像はコンペ終了後にお渡ししますので仮の画像を入れていただければと思います。
商品画像以外の使用素材は有料のものでも問題は有りませんが、kirova framesまたは低価格(0~2000円程度)のものでお願いします。
※もし有料素材を使う場合は最初から購入して頂く必要はないのでウォーターマーク付きのもので提案していただければ大丈夫です。

<デザイン>
明るめのやさしい感じでお願いします。
参考サイトほどピンクは強めでなくてもいいかと思いますが、デザイン次第では濃い色の使用もありかと思います。

参考サイト
https://pelvantri.jp/

<ページ幅>
1920pxでお願いします。

<特筆事項>
今回TOLUを使用するにあたりプラン的にTOLUマークが必須になります。
右上のテントのマークはありきでお願いします。

今後も定期的にデザインをお願いすることができる技量を持つ方を探しておりますので是非、単発と考えずにデザインを出していただければと思います。
それでは皆様のご応募よろしくお願い致します。
ページ数
1ページ
希望イメージ
シンプル 複雑
単色 カラフル
暗い 明るい
日常 高級
遊び心 厳粛
未来的 伝統的
女性的 男性的
希望する色
白・淡いピンク・淡い水色などの優しい色
納品ファイル
• フォトショップ形式 (.psd)

こちらが想定した以上のデザインでした。

この度は当方コンペにご提案いただきありがとうございました。
提案頂いた方々のデザインはどれも素敵なもので、真剣に吟味し当選者を選択させていただきました。
今後もピオネッタを利用してのデザインコンペを行う予定ですので、残念ながら今回は当選とならなかった方もまたご参加いただけると幸いです。
今後もどうかよろしくお願い致します。

```html
<!DOCTYPE html>
<html lang="ja">
<head>
<meta charset="utf-8">
<title>lumiette</title>
<link href="https://fonts.googleapis.com/css2?family=Josefin+Sans:wght@300;400&family=Noto+Sans+JP:wght@300;400;500&display=swap" rel="stylesheet">
<style>
:root{
  --pink:#f2a3ab;
  --pink-deep:#ef8790;
  --blush:#fbe2e2;
  --paper:#fdf1f1;
  --white:#ffffff;
  --ink:#6b5558;
  --ink-soft:#9a8285;
  --badge:#e9c7c9;
}
*{margin:0;padding:0;box-sizing:border-box}
html,body{width:1200px;height:2168px;overflow:hidden}
body{background:var(--blush);font-family:"Noto Sans JP",sans-serif;color:var(--ink);position:relative}
.site-header{position:absolute;top:0;left:0;width:1200px;height:64px;background:var(--pink);display:flex;align-items:center;padding:0 120px 0 150px}
.brand{font-family:"Josefin Sans",sans-serif;font-weight:400;font-size:30px;color:var(--white);letter-spacing:1px}
.nav{display:flex;gap:44px;margin-left:270px;font-size:12px;color:var(--white);letter-spacing:1px;white-space:nowrap}
.header-icons{display:flex;gap:14px;margin-left:auto;align-items:center}
.hero{position:absolute;top:64px;left:0;width:1200px;height:576px;background:linear-gradient(120deg,#f3d6d2 0%,#efcfcb 40%,#f6e2de 70%,#ecc8c3 100%)}
.hero-copy{position:absolute;left:370px;top:270px;color:var(--white)}
.hero-title{font-family:"Josefin Sans",sans-serif;font-weight:300;font-size:92px;line-height:1;letter-spacing:2px}
.hero-sub{font-size:22px;letter-spacing:6px;margin-top:10px}
.hero-note{font-size:12px;letter-spacing:2px;margin-top:10px;opacity:.9}
.sdgs{position:absolute;top:640px;left:0;width:1200px;height:192px;background:var(--paper);display:flex;align-items:center;padding:0 160px 0 200px}
.sdgs-badge{text-align:center;width:96px;flex-shrink:0}
.sdgs-mark{width:64px;height:64px;border-radius:50%;background:var(--badge);margin:0 auto 8px}
.sdgs-label{font-size:12px;line-height:1.5;color:var(--ink)}
.sdgs-text{margin-left:44px;font-size:12px;line-height:2.1;color:var(--ink-soft);width:700px}
.products{position:absolute;top:832px;left:0;width:1200px;height:948px;background:var(--pink)}
.product-grid{display:grid;grid-template-columns:592px 592px;grid-template-rows:380px 384px;gap:16px;background:var(--blush)}
.product-tile{background:var(--pink);position:relative}
.product-photo{position:absolute;left:108px;top:56px;width:372px;height:272px}
.photo-ballet{background:linear-gradient(135deg,#e9e6dc,#c8cfb9 55%,#e4dbd2)}
.photo-room{background:linear-gradient(135deg,#6e706e,#4e4f50 60%,#8b8b89)}
.photo-spray{background:linear-gradient(135deg,#f0ede6,#d8d6cd 55%,#b8b7ae)}
.photo-mask{background:linear-gradient(135deg,#d9dbe0,#e8e9ec 55%,#c3c6cc)}
.product-label{position:absolute;left:180px;top:120px;width:190px;height:40px;background:rgba(255,255,255,.25);border:1px solid rgba(255,255,255,.8);display:flex;align-items:center;justify-content:center;gap:10px;color:var(--white);font-size:14px;letter-spacing:1px;white-space:nowrap}
.more-button{position:absolute;left:452px;top:828px;width:292px;height:68px;border-radius:34px;background:var(--pink-deep);color:var(--white);display:flex;align-items:center;justify-content:center;gap:14px;font-size:16px;letter-spacing:2px}
.links{position:absolute;top:1780px;left:0;width:1200px;height:240px;background:var(--blush)}
.link-item{position:absolute;top:60px;width:160px;text-align:center;font-size:14px;color:var(--ink)}
.link-item svg{display:block;margin:0 auto 14px}
.site-footer{position:absolute;top:2020px;left:0;width:1200px;height:148px;background:var(--pink);color:var(--white);text-align:center}
.footer-links{display:flex;justify-content:center;gap:90px;font-size:11px;margin-top:52px}
.copyright{font-size:10px;margin-top:30px}
</style>
</head>
<body>
<header class="site-header">
  <div class="brand">lumiette</div>
  <nav class="nav"><span>HOME</span><span>商品一覧</span><span>ブランド紹介</span><span>お問い合わせ</span></nav>
  <div class="header-icons">
    <svg width="22" height="20" viewBox="0 0 22 20" fill="none" stroke="#fff" stroke-width="1.6"><path d="M1 2h3l3 11h11l2-8H6"/><circle cx="9" cy="17" r="1.5"/><circle cx="16" cy="17" r="1.5"/></svg>
    <svg width="14" height="14"><rect width="14" height="14" fill="none" stroke="#fff" stroke-width="1.6"/></svg>
  </div>
</header>

<section class="hero" role="img" aria-label="ピンクの背景にバレエシューズ、香水、パール、花を並べた写真">
  <div class="hero-copy">
    <div class="hero-title">lumiette</div>
    <div class="hero-sub">やさしい毎日を</div>
    <div class="hero-note">心地よい暮らしに寄り添うアイテムをお届けします</div>
  </div>
</section>

<section class="sdgs">
  <div class="sdgs-badge"><div class="sdgs-mark"></div><div class="sdgs-label">SDGs<br>への取り組み</div></div>
  <p class="sdgs-text">私たちは持続可能な社会の実現に向けて、環境にやさしい素材選びと丁寧なものづくりを続けています。長く使える品質の商品をお届けし、無駄の少ない暮らしを応援します。包装資材の削減やリサイクル素材の活用にも取り組み、地域やお客様とともに未来へつながる活動を広げてまいります。日々の小さな選択が、やさしい未来をつくると信じています。</p>
</section>

<section class="products">
  <div class="product-grid">
    <div class="product-tile"><div class="product-photo photo-ballet" role="img" aria-label="バレエシューズと白い花の写真"></div><div class="product-label">バレエシューズ <span>→</span></div></div>
    <div class="product-tile"><div class="product-photo photo-room" role="img" aria-label="グレーのルームシューズの写真"></div><div class="product-label">ルームシューズ <span>→</span></div></div>
    <div class="product-tile"><div class="product-photo photo-spray" role="img" aria-label="除菌スプレーのボトルの写真"></div><div class="product-label">Ag+除菌スプレー <span>→</span></div></div>
    <div class="product-tile"><div class="product-photo photo-mask" role="img" aria-label="白いマスクケースの写真"></div><div class="product-label">マスクケース <span>→</span></div></div>
  </div>
  <div class="more-button">商品一覧 <span>→</span></div>
</section>

<section class="links">
  <div class="link-item" style="left:192px">
    <svg width="48" height="48" viewBox="0 0 48 48" fill="#ef8790"><rect x="6" y="10" width="20" height="34"/><rect x="26" y="20" width="16" height="24"/><g fill="#fbe2e2"><rect x="11" y="16" width="4" height="4"/><rect x="18" y="16" width="4" height="4"/><rect x="11" y="25" width="4" height="4"/><rect x="18" y="25" width="4" height="4"/><rect x="31" y="26" width="4" height="4"/><rect x="31" y="34" width="4" height="4"/></g></svg>
    会社概要
  </div>
  <div class="link-item" style="left:520px">
    <svg width="48" height="48" viewBox="0 0 48 48" fill="#ef8790"><path d="M12 6l7 8-4 5c2 5 6 9 11 11l5-4 8 7-5 7C20 40 6 26 6 12z"/><path d="M28 6a14 14 0 0 1 14 14h-4A10 10 0 0 0 28 10z"/></svg>
    お問い合わせ
  </div>
  <div class="link-item" style="left:812px">
    <svg width="48" height="48" viewBox="0 0 48 48" fill="#ef8790"><path d="M24 6c10 0 18 7 18 15s-8 15-18 15l-10 7 2-9C9 31 6 26 6 21 6 13 14 6 24 6z"/><text x="24" y="27" font-size="14" text-anchor="middle" fill="#fbe2e2" font-family="sans-serif">Q</text></svg>
    お問い合わせ
  </div>
</section>

<footer class="site-footer">
  <div class="footer-links"><span>特定商取引法に基づく表記</span><span>プライバシーポリシー</span></div>
  <div class="copyright">© lumiette</div>
</footer>
</body>
</html>
```